Box and Paper Bag Design
for exclusive line of prescriptions creams
Box and Paper Bag Design  - Health
Creative Brief
A design for the box (layout attached) and a promotional paper bag (no layout - see sample picture: 8" length, 7" high, 3.5" deep) - front and back designs will be fine. Both packages are for exclusive line of prescription creams. Should resemble expensive, high end, sophisticated and upscale style, yet THIS IS PRESCRIPTION MEDICATION - the packaging should resemble this also. FRONT: 1. Logo (attached) 2. Text: Professional Prescription Formula Dispensed Only By Physicians 3. On the bottom: e 30 ml / 1 fl.oz. Made in USA BACK: All the way on the bottom - try to fit into lower 1/4th of the space: Directions: Follow the directions of your prescribing Physician Cautions: For external use only - do not ingest. Avoid contact with open wounds. Avoid getting into eyes. Make sure skin is clean and dry before applying . Discontinue use if rash or discomfort occurs. Not for use by pregnant or lactating women. The packaging is NOT child resistant. KEEP AWAY FROM CHILDREN. If accidentally ingested seek medical help immediately. _________________________ We will be using various technics while printing the boxes: uv coating, spot foil etc See several samples of the designs I liked attached. Try to stick to conservative yet fresh colors: metallic, silver, gray , blue, green.
Health
Doctors, medical professionals and their patients.

```html
<!DOCTYPE html>
<html lang="en">
<head>
<meta charset="utf-8">
<title>Caldorine – Box Dieline</title>
<link href="https://fonts.googleapis.com/css2?family=Josefin+Sans:wght@300&family=Libre+Baskerville:ital,wght@0,400;1,700&display=swap" rel="stylesheet">
<style>
  :root {
    --page: #ffffff;
    --gold: #f1cf45;
    --gold-light: #f8e27c;
    --brown: #a54f0c;
    --rust: #b4530f;
    --ink: #3a2a12;
    --name: #3b3b3b;
    --cream: #fbeed0;
    --cut: #6b6b6b;
    --rule: #c9a640;
  }
  html, body { margin: 0; padding: 0; overflow: hidden; background: var(--page); }
  .dieline { display: block; width: 1200px; height: 975px; }
  .brand-name { font-family: "Josefin Sans", sans-serif; font-weight: 300; fill: var(--name); font-size: 7px; letter-spacing: 1.4px; }
  .tagline { font-family: "Libre Baskerville", serif; font-style: italic; font-weight: 700; fill: var(--ink); font-size: 4.1px; }
  .tagline-small { font-family: "Libre Baskerville", serif; font-style: italic; font-weight: 700; fill: var(--ink); font-size: 2.4px; }
  .volume { font-family: "Libre Baskerville", serif; font-weight: 400; font-size: 2.9px; fill: var(--ink); }
  .caution-text { font-family: "Libre Baskerville", serif; font-weight: 400; font-size: 1.55px; fill: var(--cream); }
  .flap { fill: #ffffff; stroke: var(--cut); stroke-width: 0.35; }
  .fold { stroke: var(--cut); stroke-width: 0.3; }
  .rule { stroke: var(--rule); stroke-width: 0.3; }
</style>
</head>
<body>
<svg class="dieline" viewBox="0 0 454 369" preserveAspectRatio="none" xmlns="http://www.w3.org/2000/svg">
  <defs>
    <linearGradient id="goldPanel" x1="0" y1="0" x2="1" y2="0">
      <stop offset="0" stop-color="#f1cf45"/>
      <stop offset="0.5" stop-color="#f8e27c"/>
      <stop offset="1" stop-color="#f1cf45"/>
    </linearGradient>
    <g id="frontCopy">
      <text class="tagline" text-anchor="middle" y="0">Professional Prescription Formula</text>
      <text class="tagline" text-anchor="middle" y="6">Dispensed Only By Physicians</text>
    </g>
    <g id="cautionBlock">
      <rect width="68" height="23" fill="#b4530f" stroke="#e7b04a" stroke-width="0.3"/>
      <text class="caution-text" x="2" y="3.6">Directions: Follow the directions of your prescribing Physician.</text>
      <text class="caution-text" x="2" y="6.6">Cautions: For external use only - do not ingest. Avoid contact with</text>
      <text class="caution-text" x="2" y="9.6">open wounds. Avoid getting into eyes. Make sure skin is clean and</text>
      <text class="caution-text" x="2" y="12.6">dry before applying. Discontinue use if rash or discomfort occurs.</text>
      <text class="caution-text" x="2" y="15.6">Not for use by pregnant or lactating women. The packaging is NOT</text>
      <text class="caution-text" x="2" y="18.6">child resistant. KEEP AWAY FROM CHILDREN. If accidentally</text>
      <text class="caution-text" x="2" y="21.6">ingested seek medical help immediately.</text>
    </g>
  </defs>

  <!-- glue flap -->
  <path class="flap" d="M28 130 L0 142 L0 248 L28 258 Z"/>

  <!-- dust flaps -->
  <path class="flap" d="M133 130 L133 88 L228 88 L238 108 L238 130 Z"/>
  <path class="flap" d="M345 130 L345 108 L355 88 L454 88 L454 130 Z"/>
  <path class="flap" d="M28 258 L28 280 L40 282 L133 282 L133 258 Z"/>
  <path class="flap" d="M345 258 L345 282 L443 282 L454 270 L454 258 Z"/>

  <!-- top lid -->
  <g class="top-lid">
    <path d="M28 14 Q28 0 42 0 L119 0 Q133 0 133 14 Z" fill="var(--brown)"/>
    <rect x="28" y="14" width="105" height="98" fill="url(#goldPanel)"/>
    <rect x="28" y="112" width="105" height="18" fill="var(--brown)"/>
    <line class="rule" x1="28" y1="110" x2="133" y2="110"/>
    <g transform="rotate(180 80.5 57)">
      <text class="brand-name" text-anchor="middle" x="80.5" y="63">CALDORINE</text>
      <text class="tagline-small" text-anchor="middle" x="80.5" y="97">Professional Prescription Formula Dispensed Only By Physicians</text>
    </g>
  </g>

  <!-- body panels -->
  <g class="box-body">
    <rect x="28" y="130" width="426" height="17" fill="var(--brown)"/>
    <rect x="28" y="147" width="426" height="93" fill="url(#goldPanel)"/>
    <rect x="28" y="240" width="426" height="18" fill="var(--brown)"/>
    <line class="rule" x1="28" y1="149" x2="454" y2="149"/>
    <line class="rule" x1="28" y1="227" x2="454" y2="227"/>
    <line class="fold" x1="133" y1="130" x2="133" y2="258"/>
    <line class="fold" x1="238" y1="130" x2="238" y2="258"/>
    <line class="fold" x1="345" y1="130" x2="345" y2="258"/>
  </g>

  <!-- bottom lid -->
  <path d="M238 258 L345 258 L345 355 Q345 369 331 369 L252 369 Q238 369 238 355 Z" fill="var(--brown)"/>

  <!-- front panel -->
  <g class="front-panel">
    <text class="brand-name" text-anchor="middle" x="80.5" y="182">CALDORINE</text>
    <use href="#frontCopy" x="80.5" y="204"/>
    <text class="volume" text-anchor="middle" x="80.5" y="235">e 30 ml / 1 fl.oz. Made in USA</text>
  </g>

  <!-- back panel -->
  <g class="back-panel">
    <text class="brand-name" text-anchor="middle" x="185.5" y="182">CALDORINE</text>
    <use href="#cautionBlock" x="151.5" y="196"/>
  </g>

  <!-- second front panel -->
  <g class="front-panel">
    <text class="brand-name" text-anchor="middle" x="291.5" y="182">CALDORINE</text>
    <use href="#frontCopy" x="291.5" y="204"/>
    <text class="volume" text-anchor="middle" x="291.5" y="235">e 30 ml / 1 fl.oz. Made in USA</text>
  </g>

  <!-- second back panel -->
  <g class="back-panel">
    <text class="brand-name" text-anchor="middle" x="399.5" y="182">CALDORINE</text>
    <use href="#cautionBlock" x="365.5" y="196"/>
  </g>
</svg>
</body>
</html>
```